Marlowe Tindra Pale Ale Beer Label/Badge

We need a Beer Label designed for our first official beer to be launched under The marlowe Brand!!
It will be a Pale Ale Called "Tindra Pale Ale"!

The Marlowe has the largest Craft Beer & Cider selection in the Geelong & Surf Coast region. With a funky location and a relaxed vibe, Marlowe prides itself on serving delicious, unique seasonal food paired with Australia's best Craft Beer. The marlowe is the perfect setting for a relaxed afternoon or evening with friends and can package an experience for larger groups or corporate bookings.

The Marlowe Tavern brand has been growing for over a year and a half and the first label needs to integrate The marlowe Logo but at the same time bring a fresh, new and eye catching feel to it along with embracing the "Odysseus" story in which we will be naming future beers.

The story of Tindra is found via the following link
http://en.lorevault.example/wiki/Tindra_(legend)

We expect designers to research The marlowe Tavern brand along with the all important Craft Beer Market and demographics. This will, potentially, be the start of many more labels to come for the winning designer!!

Requirements
Must have
• The original "O" needs to be integrated into the new logo and as much as the Greek mythology is being used it needs to be certain that this is an original Australian Craft Beer in the modern age!!
strong, modern & unique!!
Nice to have
• Logo could have a depiction of Tindra
Should not have
• tackiness or cheap!!

```html
<!DOCTYPE html>
<html lang="en">
<head>
<meta charset="utf-8">
<title>Marlowe Tindra Pale Ale — Label</title>
<link rel="stylesheet" href="https://fonts.googleapis.com/css2?family=Quicksand:wght@500;700&family=Cinzel:wght@700&display=swap">
<style>
  :root {
    --bg: #f4f1e4;
    --label-cream: #fdfbc8;
    --label-glow: #fff7a0;
    --scallop-red: #d8222a;
    --outline: #111111;
    --badge-maroon: #8a1a1c;
    --banner-fill: #5a1214;
    --banner-text: #e4e6ea;
    --ink: #2a2a2a;
  }
  html, body {
    margin: 0;
    padding: 0;
    width: 1200px;
    height: 1000px;
    overflow: hidden;
    background: var(--bg);
  }
  .label-canvas {
    display: block;
    width: 1200px;
    height: 1000px;
  }
  .neck-name, .center-name {
    font-family: "Quicksand", sans-serif;
    font-weight: 700;
    fill: var(--label-cream);
  }
  .neck-tagline {
    font-family: "Quicksand", sans-serif;
    font-weight: 700;
    font-size: 30px;
    fill: var(--ink);
  }
  .origin-arc {
    font-family: "Quicksand", sans-serif;
    font-weight: 500;
    font-size: 24px;
    fill: var(--ink);
    letter-spacing: 1px;
  }
  .beer-name {
    font-family: "Cinzel", serif;
    font-weight: 700;
    font-size: 96px;
    fill: var(--banner-text);
    letter-spacing: 6px;
  }
  .beer-style {
    font-family: "Quicksand", sans-serif;
    font-weight: 700;
    font-size: 30px;
    fill: var(--ink);
    letter-spacing: 1px;
  }
  .abv {
    font-family: "Quicksand", sans-serif;
    font-weight: 500;
    font-size: 20px;
    fill: var(--ink);
  }
</style>
</head>
<body>
<svg class="label-canvas" viewBox="0 0 1200 1000" xmlns="http://www.w3.org/2000/svg">
  <defs>
    <radialGradient id="label-face" cx="50%" cy="50%" r="55%">
      <stop offset="0%" stop-color="#ffffff"/>
      <stop offset="55%" stop-color="var(--label-cream)"/>
      <stop offset="100%" stop-color="var(--label-glow)"/>
    </radialGradient>
    <path id="origin-path" d="M 430 600 A 170 170 0 0 1 770 600"/>
  </defs>

  <!-- Neck label -->
  <g class="neck-label">
    <circle cx="600" cy="150" r="72" fill="var(--badge-maroon)"/>
    <text class="neck-name" x="600" y="160" font-size="28" text-anchor="middle">Marlowe</text>
    <text class="neck-tagline" x="600" y="270" text-anchor="middle">Handcrafted Beer</text>
  </g>

  <!-- Body label -->
  <g class="body-label">
    <ellipse cx="600" cy="620" rx="330" ry="300" fill="var(--outline)"/>
    <ellipse cx="600" cy="620" rx="318" ry="288" fill="var(--scallop-red)"/>
    <ellipse cx="600" cy="620" rx="282" ry="252" fill="url(#label-face)"/>

    <text class="origin-arc" text-anchor="middle">
      <textPath href="#origin-path" startOffset="50%">Ferncliff Ridge, Victoria, Australia</textPath>
    </text>

    <circle cx="600" cy="555" r="58" fill="var(--scallop-red)"/>
    <text class="center-name" x="600" y="563" font-size="22" text-anchor="middle">Marlowe</text>

    <g class="name-banner">
      <rect x="170" y="612" width="860" height="104" rx="52" fill="var(--outline)"/>
      <rect x="180" y="622" width="840" height="84" rx="42" fill="var(--banner-fill)"/>
      <text class="beer-name" x="600" y="698" text-anchor="middle">TINDRA</text>
    </g>

    <text class="beer-style" x="600" y="762" text-anchor="middle">PALE ALE BEER</text>
    <text class="abv" x="600" y="842" text-anchor="middle">ABV 5%</text>
  </g>
</svg>
</body>
</html>
```